Task Description: Full Vehicle Wrap Design for Brisk Owl – Rodent & Exclusion Company
We’re launching a design contest for a full vehicle wrap for Brisk Owl, our rodent control and exclusion company. We’re looking for a design that is bold, clean, and communicates what we do — while also standing out on the road.

About the Company
Before you start designing, please visit our website: www.BriskOwlUSA.com. Learn what we do and how we serve homeowners. Understanding our mission will help your design align with our brand and services.

Vehicles in Our Fleet
We're looking for wraps that will be consistent across multiple vehicles in our fleet:

16-foot Box Truck

Side Panels: 16 ft wide x 8 ft tall

Back Door: 8 ft wide x 8 ft tall

Note: The back of the truck is critical — it’s what drivers behind us see most, so that space must clearly and simply convey our service and name.

2016 Velmar Drover Span Cargo LX

Please look up this model online for reference.

Smaller van, perfect for mobile service calls. Needs a complementary design to the box truck.

2020 Velmar T-340 LX

Optional third vehicle. A clean, scaled-down version of the box truck or van design would be ideal for consistency.

Design Direction
We’ve uploaded a file with three visual examples of directions we like. Please review all three and choose the one that resonates most with your artistic style. Don’t try to blend all three — we want to see how your creativity builds on the one you connect with most.

The goal is:

Brand recognition

Clear messaging (what we do, who we are)

Clean, modern, eye-catching — not cluttered

Ideally: something that can be extended or scaled across the different vehicle sizes

```html
<!DOCTYPE html>
<html lang="en">
<head>
<meta charset="utf-8">
<title>Brisk Owl – Box Truck Wrap Panels</title>
<link href="https://fonts.googleapis.com/css2?family=Montserrat:wght@400;500;600;700;800&family=Roboto+Slab:wght@800&display=swap" rel="stylesheet">
<style>
  :root {
    --charcoal: #262626;
    --charcoal-deep: #1b1b1b;
    --orange: #f0651f;
    --orange-light: #f7893f;
    --white: #ffffff;
    --page: #ffffff;
  }
  html, body {
    margin: 0;
    width: 1200px;
    height: 1200px;
    overflow: hidden;
    background: var(--page);
  }
  .canvas {
    position: relative;
    width: 1200px;
    height: 1200px;
    font-family: "Montserrat", Arial, sans-serif;
  }
  .panel { position: absolute; display: block; }
  .side-left  { left: 40px;  top: 40px;  width: 820px; height: 360px; }
  .side-right { left: 340px; top: 440px; width: 820px; height: 360px; }
  .back-door  { left: 790px; top: 845px; width: 360px; height: 340px; }
  .cab-header { left: 60px;  top: 960px; width: 460px; height: 110px; }

  .brand-name  { font-family: "Montserrat", Arial, sans-serif; font-weight: 500; fill: var(--orange); letter-spacing: 3px; }
  .tagline     { font-weight: 700; fill: var(--white); }
  .tagline .hl { fill: var(--orange); }
  .offer-text  { font-family: "Roboto Slab", Georgia, serif; font-weight: 800; letter-spacing: 1px; }
  .phone       { font-weight: 800; fill: var(--white); letter-spacing: 0.5px; }
  .headline    { font-weight: 700; fill: var(--white); }
  .small-bold  { font-weight: 800; fill: var(--white); }
  .perk        { font-weight: 700; fill: var(--white); font-size: 9.5px; letter-spacing: 0.2px; }
  .bullet      { font-weight: 600; fill: var(--white); font-size: 7.2px; }
  .sub-regular { font-weight: 400; fill: var(--white); }
</style>
</head>
<body>
<div class="canvas">

  <svg width="0" height="0" style="position:absolute">
    <defs>
      <linearGradient id="houseTone" x1="0" y1="0" x2="1" y2="1">
        <stop offset="0" stop-color="#f58a45"/>
        <stop offset="1" stop-color="#e2561a"/>
      </linearGradient>
      <radialGradient id="ratTone" cx="0.5" cy="0.55" r="0.6">
        <stop offset="0" stop-color="#7a5a40"/>
        <stop offset="1" stop-color="#2d241d"/>
      </radialGradient>
      <g id="noMark">
        <circle r="9" fill="var(--white)"/>
        <line x1="-6" y1="6" x2="6" y2="-6" stroke="var(--charcoal)" stroke-width="2.2"/>
      </g>
      <g id="tickBox">
        <rect x="-6" y="-6" width="12" height="12" fill="none" stroke="var(--white)" stroke-width="1.6"/>
        <path d="M-3.5 0 L-1 2.8 L4 -3" fill="none" stroke="var(--white)" stroke-width="1.8"/>
      </g>
    </defs>
  </svg>

  <!-- Side panel: driver side -->
  <svg class="panel side-left" viewBox="0 0 820 360" aria-label="Brisk Owl box truck side panel">
    <rect width="820" height="360" fill="var(--charcoal)"/>
    <path d="M0 0 H150 Q108 115 160 232 H0 Z" fill="url(#houseTone)" role="img" aria-label="Photo of a suburban house roofline tinted orange"/>
    <path d="M176 0 Q130 115 182 232" fill="none" stroke="var(--orange)" stroke-width="9"/>

    <circle cx="238" cy="60" r="28" fill="var(--orange)"/>
    <text class="brand-name" x="282" y="86" font-size="64">BRISK OWL</text>

    <text class="tagline" x="234" y="122" font-size="14.5">Specializes in <tspan class="hl">rat control</tspan>, <tspan class="hl">mice control</tspan>, and <tspan class="hl">rodent-proofing</tspan></text>

    <circle cx="385" cy="186" r="44" fill="url(#ratTone)" role="img" aria-label="Photo of a brown rat"/>
    <circle cx="385" cy="186" r="44" fill="none" stroke="var(--orange)" stroke-width="6"/>
    <line x1="355" y1="155" x2="415" y2="217" stroke="var(--orange)" stroke-width="6"/>

    <rect x="452" y="138" width="262" height="32" fill="var(--orange)"/>
    <text class="offer-text" x="583" y="162" font-size="21" fill="var(--white)" text-anchor="middle">FREE INSPECTION</text>
    <text class="phone" x="452" y="214" font-size="40">510-555-0188</text>

    <use href="#noMark" x="40" y="168"/>
    <use href="#noMark" x="64" y="168"/>
    <use href="#noMark" x="88" y="168"/>
    <text class="small-bold" x="64" y="195" font-size="11" text-anchor="middle">Remove them</text>
    <text class="small-bold" x="64" y="210" font-size="13" text-anchor="middle">FOR GOOD!</text>

    <rect y="232" width="820" height="7" fill="var(--orange)"/>
    <text class="headline" x="22" y="280" font-size="33">Protect your home. Get started today!</text>
    <rect y="298" width="820" height="40" fill="var(--orange)"/>
    <use href="#tickBox" x="24" y="318"/>
    <text class="perk" x="38" y="321.5">ABSOLUTELY NO POISONS OR TOXIC CHEMICALS</text>
    <use href="#tickBox" x="356" y="318"/>
    <text class="perk" x="370" y="321.5">ONE-TIME TREATMENT</text>
    <use href="#tickBox" x="556" y="318"/>
    <text class="perk" x="570" y="321.5">LOCALLY OWNED &amp; OPERATED</text>
  </svg>

  <!-- Side panel: passenger side -->
  <svg class="panel side-right" viewBox="0 0 820 360" aria-label="Brisk Owl box truck opposite side panel">
    <rect width="820" height="360" fill="var(--charcoal)"/>
    <path d="M820 0 H670 Q712 115 660 232 H820 Z" fill="url(#houseTone)" role="img" aria-label="Photo of a suburban house roofline tinted orange"/>
    <path d="M644 0 Q690 115 638 232" fill="none" stroke="var(--orange)" stroke-width="9"/>

    <circle cx="86" cy="60" r="28" fill="var(--orange)"/>
    <text class="brand-name" x="132" y="86" font-size="64">BRISK OWL</text>

    <text class="tagline" x="60" y="122" font-size="14.5">Specializes in <tspan class="hl">rat control</tspan>, <tspan class="hl">mice control</tspan>, and <tspan class="hl">rodent-proofing</tspan></text>

    <rect x="60" y="138" width="262" height="32" fill="var(--orange)"/>
    <text class="offer-text" x="191" y="162" font-size="21" fill="var(--white)" text-anchor="middle">FREE INSPECTION</text>
    <text class="phone" x="60" y="214" font-size="40">510-555-0188</text>

    <circle cx="440" cy="186" r="44" fill="url(#ratTone)" role="img" aria-label="Photo of a brown rat"/>
    <circle cx="440" cy="186" r="44" fill="none" stroke="var(--orange)" stroke-width="6"/>
    <line x1="410" y1="155" x2="470" y2="217" stroke="var(--orange)" stroke-width="6"/>

    <use href="#noMark" x="732" y="168"/>
    <use href="#noMark" x="756" y="168"/>
    <use href="#noMark" x="780" y="168"/>
    <text class="small-bold" x="756" y="195" font-size="11" text-anchor="middle">Remove them</text>
    <text class="small-bold" x="756" y="210" font-size="13" text-anchor="middle">FOR GOOD!</text>

    <rect y="232" width="820" height="7" fill="var(--orange)"/>
    <text class="headline" x="22" y="280" font-size="33">Protect your home. Get started today!</text>
    <rect y="298" width="820" height="40" fill="var(--orange)"/>
    <use href="#tickBox" x="24" y="318"/>
    <text class="perk" x="38" y="321.5">ABSOLUTELY NO POISONS OR TOXIC CHEMICALS</text>
    <use href="#tickBox" x="356" y="318"/>
    <text class="perk" x="370" y="321.5">ONE-TIME TREATMENT</text>
    <use href="#tickBox" x="556" y="318"/>
    <text class="perk" x="570" y="321.5">LOCALLY OWNED &amp; OPERATED</text>
  </svg>

  <!-- Cab roof fairing mark -->
  <svg class="panel cab-header" viewBox="0 0 460 110" aria-label="Brisk Owl cab roof lettering">
    <circle cx="70" cy="55" r="22" fill="var(--orange)"/>
    <text class="brand-name" x="106" y="74" font-size="50">BRISK OWL</text>
  </svg>

  <!-- Rear door panel -->
  <svg class="panel back-door" viewBox="0 0 360 340" aria-label="Brisk Owl box truck rear door panel">
    <rect width="360" height="340" fill="var(--charcoal)"/>
    <path d="M0 118 Q180 62 360 92 V340 H0 Z" fill="var(--orange)"/>
    <path d="M318 2 Q346 26 358 64" fill="none" stroke="var(--orange)" stroke-width="5"/>

    <circle cx="62" cy="50" r="19" fill="var(--orange)"/>
    <text class="brand-name" x="92" y="62" font-size="32" letter-spacing="1.5">BRISK OWL</text>

    <line x1="180" y1="100" x2="180" y2="340" stroke="var(--charcoal-deep)" stroke-width="1.2" opacity="0.6"/>

    <text class="headline" x="16" y="150" font-size="14">Protect your home.</text>
    <text class="sub-regular" x="24" y="168" font-size="14">Get started today!</text>

    <g transform="translate(0 2) scale(0.75)">
      <use href="#noMark" x="90" y="258"/>
      <use href="#noMark" x="114" y="258"/>
      <use href="#noMark" x="138" y="258"/>
    </g>
    <text class="small-bold" x="85" y="216" font-size="8.5" text-anchor="middle">Remove them</text>
    <text class="small-bold" x="85" y="228" font-size="10" text-anchor="middle">FOR GOOD!</text>

    <circle cx="80" cy="282" r="44" fill="url(#ratTone)" role="img" aria-label="Photo of a brown rat"/>
    <circle cx="80" cy="282" r="44" fill="none" stroke="var(--charcoal)" stroke-width="5"/>
    <line x1="50" y1="251" x2="110" y2="313" stroke="var(--charcoal)" stroke-width="5"/>

    <rect x="190" y="130" width="156" height="20" fill="var(--white)"/>
    <text class="offer-text" x="268" y="145" font-size="12.5" fill="var(--orange)" text-anchor="middle">FREE INSPECTION</text>
    <text class="phone" x="190" y="172" font-size="19.5">510-555-0188</text>

    <g class="bullets">
      <text class="bullet" x="190" y="190">•  Professional Rodent Exclusion</text>
      <text class="bullet" x="197" y="199">Experts.</text>
      <text class="bullet" x="190" y="210">•  Over 12,000 customers serviced with</text>
      <text class="bullet" x="197" y="219">a 97% customer satisfaction rating.</text>
      <text class="bullet" x="190" y="230">•  Bay Area Local.</text>
      <text class="bullet" x="190" y="241">•  Family Owned &amp; Operated.</text>
      <text class="bullet" x="190" y="252">•  Industry Leading Warranty.</text>
      <text class="bullet" x="190" y="263">•  Comprehensive, 1x solution.</text>
      <text class="bullet" x="190" y="274">•  Eco-friendly, non-toxic materials.</text>
      <text class="bullet" x="190" y="285">•  Built primarily on word of mouth</text>
      <text class="bullet" x="197" y="294">referrals.</text>
      <text class="bullet" x="190" y="305">•  Fast availability.</text>
    </g>
  </svg>

</div>
</body>
</html>
```